Wedding Decor and Entertianment business card

Company - We run a weddings and events company called Amber Fern, we provide most entertainment and decor services to our customers.

Initial idea is ....
A simple business card with logo on the front, this will be spot varnish. On a matt black background.
The reverse will be simple contact information.

But happy to try things outside of the box and would welcome some crazy ideas.

Target Market(s)

wedding couples - 21 - 40
High end wedding venues.

Industry/Entity Type

Wedding

Contact Information for Business Card

01742 918 263
amberfern.co.uk
rupert@amberfern.co.uk
or
eleanor@amberfern.co.uk

Requirements
Nice to have
• black matt background with spot varnish logo on the front.

```html
<!DOCTYPE html>
<html lang="en">
<head>
<meta charset="utf-8">
<title>Amber Fern — Business Card</title>
<link rel="stylesheet" href="https://fonts.googleapis.com/css2?family=Jost:wght@300;400;600&display=swap">
<style>
  :root {
    --backdrop: #2a2a2a;
    --card-light: #f7f7f7;
    --card-dark: #161616;
    --ink-grey: #6b6b6b;
    --ink-soft: #8f8f8f;
    --accent-mauve: #8c6f8f;
    --dark-mark: #8a8a8a;
    --dark-url: #4a4a4a;
  }
  * { margin: 0; padding: 0; box-sizing: border-box; }
  html, body {
    width: 1200px; height: 873px; overflow: hidden;
    background: var(--backdrop);
    font-family: "Jost", "Futura", sans-serif;
  }
  .stage { position: relative; width: 1200px; height: 873px; }

  .card {
    position: absolute;
    width: 560px; height: 320px;
    box-shadow: 0 12px 30px rgba(0,0,0,.45);
  }

  /* Contact side */
  .card--contact { left: 60px; top: 90px; background: var(--card-light); }
  .card--contact .wordmark {
    position: absolute; left: 92px; top: 58px;
    display: flex; align-items: center; gap: 18px;
  }
  .wordmark__square {
    width: 44px; height: 44px;
    border: 3px solid var(--ink-grey);
  }
  .wordmark__name {
    font-weight: 300; font-size: 36px; letter-spacing: 12px;
    color: var(--ink-grey); text-transform: uppercase;
  }
  .person {
    position: absolute; left: 92px; top: 160px; width: 170px; text-align: right;
  }
  .person__name { font-weight: 600; font-size: 17px; color: var(--accent-mauve); }
  .person__role { font-weight: 400; font-size: 14px; color: var(--ink-grey); }
  .divider {
    position: absolute; left: 285px; top: 145px; width: 2px; height: 78px;
    background: linear-gradient(to bottom, transparent, var(--accent-mauve) 50%, transparent);
  }
  .contact-list {
    position: absolute; left: 305px; top: 158px; list-style: none;
    font-size: 14px; font-weight: 400; color: var(--ink-soft);
  }
  .contact-list li { display: flex; align-items: center; gap: 9px; height: 24px; }
  .contact-list svg { width: 13px; height: 13px; fill: var(--accent-mauve); }
  .address {
    position: absolute; left: 0; right: 0; bottom: 34px; text-align: center;
    font-weight: 600; font-size: 14px; color: var(--accent-mauve);
  }

  /* Brand side */
  .card--brand { left: 580px; top: 470px; background: var(--card-dark); }
  .card--brand .wordmark {
    position: absolute; left: 70px; top: 108px;
    display: flex; align-items: center; gap: 20px;
  }
  .card--brand .wordmark__square { width: 48px; height: 48px; border-color: var(--dark-mark); }
  .card--brand .wordmark__name { color: var(--dark-mark); font-size: 38px; }
  .website {
    position: absolute; left: 0; right: 0; top: 230px; text-align: center;
    font-size: 15px; letter-spacing: 5px; color: var(--dark-url);
  }
</style>
</head>
<body>
<main class="stage">
  <section class="card card--contact" aria-label="Contact side of the card">
    <div class="wordmark">
      <span class="wordmark__square"></span>
      <span class="wordmark__name">Amber Fern</span>
    </div>
    <div class="person">
      <p class="person__name">Rupert Hale</p>
      <p class="person__role">President</p>
    </div>
    <span class="divider"></span>
    <ul class="contact-list">
      <li>
        <svg viewBox="0 0 16 16" aria-hidden="true"><path d="M3 1l3 3-1.5 2a9 9 0 0 0 5.5 5.5L12 10l3 3-2 2C6 15 1 10 1 3z"/></svg>
        01742 918 263
      </li>
      <li>
        <svg viewBox="0 0 16 16" aria-hidden="true"><path d="M1 3h14v10H1z M1 3l7 6 7-6" fill="none" stroke="#8c6f8f" stroke-width="1.6"/></svg>
        rupert@amberfern.co.uk
      </li>
    </ul>
    <p class="address">Unit 12b Hollow Lane Farm, Derbyshire, DE45 3QT</p>
  </section>

  <section class="card card--brand" aria-label="Brand side of the card">
    <div class="wordmark">
      <span class="wordmark__square"></span>
      <span class="wordmark__name">Amber Fern</span>
    </div>
    <p class="website">www.amberfern.co.uk</p>
  </section>
</main>
</body>
</html>
```